依頼詳細
今年の仮チラシをファイル添付しておきますので、講師の肩書、名前等の確認をお願いいたします。

昨年の講演会のチラシもファイル添付しておきますので、参考にお願いいたします。

こどもさんの笑顔の写真や、家族で幸せそうにしている写真がありそうでしたら、多めに使用していただけますか。
記載項目
記載項目は基本2018年のチラシと同じですので、ファイル添付分で確認をおねがいします。(日付だけが、9月21日(土)となります。)
サイズ
A4
ページ数
片面
希望イメージ
シンプル 複雑
単色 カラフル
暗い 明るい
日常 高級
遊び心 厳粛
未来的 伝統的
女性的 男性的
希望する色
水色系、緑系、黄・オレンジ系
納品ファイル
• 高解像度JPG (.jpg)
補足説明
今年の講演会チラシにも講師二人の写真を入れる予定です。撮影できしだいファイルをおくるかたちとなります。よろしくお願いいたします。
■ 選んだ理由

イメージと合ったから。

■ 提案者全員のお礼・コメント

みなさん、ご協力ありがとうございました。

```html
<!DOCTYPE html>
<html lang="ja">
<head>
<meta charset="utf-8">
<title>こどもの栄養 こどもの姿勢 講演会</title>
<link rel="stylesheet" href="https://fonts.googleapis.com/css2?family=M+PLUS+Rounded+1c:wght@400;700;800&family=Noto+Sans+JP:wght@400;500;700&display=swap">
<style>
:root{
  --blue:#2f8fd6;
  --blue-dark:#1f5f9e;
  --orange:#f39a1e;
  --yellow:#f7d43a;
  --sky-top:#8cc9ef;
  --sky-bottom:#e8f3d2;
  --field:#9cc36a;
  --ink:#333;
  --paper:#fff;
}
*{box-sizing:border-box;margin:0;padding:0}
html,body{width:858px;height:1200px;overflow:hidden;background:var(--paper)}
body{font-family:"Noto Sans JP",sans-serif;color:var(--ink)}
.flyer{position:relative;width:858px;height:1200px;overflow:hidden;background:var(--paper)}
.hero{position:absolute;left:0;top:0;width:858px;height:480px;
  background:linear-gradient(180deg,var(--sky-top) 0%,#c4e3f5 45%,var(--sky-bottom) 75%,var(--field) 100%)}
.tagline{position:absolute;left:22px;top:28px;padding:8px 26px;border-radius:24px;
  background:var(--blue);color:#fff;font-family:"M PLUS Rounded 1c",sans-serif;font-weight:700;font-size:22px;letter-spacing:.06em}
.title{position:absolute;font-family:"M PLUS Rounded 1c",sans-serif;font-weight:800;line-height:1;
  text-shadow:0 0 6px #fff,0 0 3px #fff}
.title .small{display:block;font-size:58px}
.title .big{display:block;font-size:96px;margin-top:4px}
.title--nutrition{left:300px;top:170px;color:var(--orange)}
.title--posture{left:30px;top:260px;color:var(--blue)}
.info{position:absolute;top:495px;left:0;width:858px;height:240px}
.label{width:56px;height:56px;border-radius:50%;color:#fff;font-weight:700;font-size:17px;
  display:flex;align-items:center;justify-content:center;text-align:center}
.label--blue{background:var(--blue)}
.label--orange{background:var(--orange)}
.when{position:absolute;left:30px;top:0}
.when .label{position:absolute;left:0;top:14px}
.era{position:absolute;left:78px;top:0;font-size:15px;color:var(--blue);font-weight:700;white-space:nowrap}
.date{position:absolute;left:78px;top:18px;font-family:"M PLUS Rounded 1c",sans-serif;font-weight:800;color:var(--blue);font-size:66px;white-space:nowrap;line-height:1}
.date .dow{display:inline-block;width:38px;height:38px;border-radius:50%;background:var(--blue);color:#fff;font-size:24px;line-height:38px;text-align:center;vertical-align:middle;margin-left:6px}
.times{position:absolute;left:78px;top:92px;font-family:"M PLUS Rounded 1c",sans-serif;font-weight:800;color:var(--blue);white-space:nowrap}
.times p{font-size:38px;line-height:1.08}
.times span{font-size:26px;margin-right:14px;vertical-align:middle}
.fee{position:absolute;left:30px;top:182px;white-space:nowrap}
.fee .label{position:absolute;left:0;top:0}
.fee .price{position:absolute;left:78px;top:2px;font-family:"M PLUS Rounded 1c",sans-serif;font-weight:800;color:var(--orange);font-size:44px;line-height:1}
.fee .price small{font-size:26px}
.where{position:absolute;left:500px;top:0;width:340px}
.where .label{position:absolute;left:0;top:14px}
.venue{position:absolute;left:72px;top:16px;color:var(--blue);font-weight:700;font-size:27px;line-height:1.25;white-space:nowrap}
.address{position:absolute;left:72px;top:96px;font-size:12px;line-height:1.6;color:var(--ink);white-space:nowrap}
.intro{position:absolute;left:90px;top:748px;width:680px;text-align:center;font-size:14px;line-height:1.75;color:var(--ink)}
.speaker{position:absolute;top:830px;width:150px;text-align:center}
.speaker--left{left:143px}
.speaker--right{left:566px}
.portrait{width:150px;height:112px;background:linear-gradient(160deg,#7a7a7a,#5c5c5c)}
.speaker .role{font-size:14px;color:var(--ink);margin-top:8px}
.speaker .name{font-size:15px;font-weight:700;color:var(--blue-dark)}
.speaker .name span{font-weight:400;font-size:12px}
.speaker .bio{position:absolute;top:10px;width:120px;font-size:10px;line-height:1.5;color:var(--ink);text-align:left}
.speaker--left .bio{left:-132px}
.speaker--right .bio{left:162px}
.cross{position:absolute;left:379px;top:838px}
.contact{position:absolute;left:0;top:1020px;width:858px;padding:0 22px}
.contact .row{display:flex;align-items:baseline;gap:22px;border-bottom:3px solid var(--blue);padding-bottom:6px}
.contact .heading{font-weight:700;font-size:18px;color:var(--blue-dark)}
.contact .tel{font-family:"M PLUS Rounded 1c",sans-serif;font-weight:800;font-size:32px;color:var(--blue-dark);letter-spacing:.02em}
.contact .tel small{font-size:16px;font-weight:700}
.organizer{font-size:12px;line-height:1.7;padding-top:8px;color:var(--ink)}
</style>
</head>
<body>
<main class="flyer">
  <section class="hero" role="img" aria-label="青空と黄色い花畑の中で笑う男の子の写真"></section>
  <p class="tagline">こども達の輝かしい未来のために</p>
  <h1>
    <span class="title title--nutrition"><span class="small">こどもの</span><span class="big">栄養</span></span>
    <span class="title title--posture"><span class="small">こどもの</span><span class="big">姿勢</span></span>
  </h1>

  <section class="info">
    <div class="when">
      <div class="label label--blue">日時</div>
      <p class="era">令和元年</p>
      <p class="date">9月21日<span class="dow">土</span></p>
      <div class="times">
        <p><span>開演</span>13:30</p>
        <p><span>開場</span>13:00</p>
      </div>
    </div>
    <div class="fee">
      <div class="label label--orange">料金</div>
      <p class="price">4000<small>円</small></p>
    </div>
    <div class="where">
      <div class="label label--blue">場所</div>
      <p class="venue">みらいプラザ<br>京都2階ホール</p>
      <p class="address">〒600-0000<br>京都府京都市下京区中央通1丁目2番地<br>京都駅より徒歩約5分<br>※駐車場はございません</p>
    </div>
  </section>

  <p class="intro">平成17年に食育基本法が制定されてはや14年。<br>長年学校教育で児童の栄養指導を行ってきたこどもの栄養専門家と<br>大学で姿勢の専門家を務めてきた博士が講演するコラボレーション講演会</p>

  <div class="speaker speaker--left">
    <div class="portrait" role="img" aria-label="講師 高野美咲さんの写真"></div>
    <p class="role">管理栄養士</p>
    <p class="name">高野 美咲 <span>さん</span></p>
    <p class="bio">学校給食に携わり二十年以上、こどもの食育を研究。</p>
  </div>
  <svg class="cross" width="100" height="100" viewBox="0 0 100 100" aria-hidden="true">
    <path d="M14 14 L86 86" stroke="var(--blue)" stroke-width="18" stroke-linecap="round"/>
    <path d="M86 14 L14 86" stroke="var(--yellow)" stroke-width="18" stroke-linecap="round"/>
  </svg>
  <div class="speaker speaker--right">
    <div class="portrait" role="img" aria-label="講師 北川誠さんの写真"></div>
    <p class="role">健康科学博士</p>
    <p class="name">北川 誠 <span>さん</span></p>
    <p class="bio">こどもの姿勢と体の発達について大学で研究を続ける。</p>
  </div>

  <footer class="contact">
    <div class="row">
      <p class="heading">●お問い合わせ</p>
      <p class="tel">075-000-1234 <small>(担当:山田)</small></p>
    </div>
    <p class="organizer">主催:京都こどもの未来を考える会　後援:ひだまり子育てネット<br>〒600-0000 京都府京都市下京区中央通1丁目2番地</p>
  </footer>
</main>
</body>
</html>
```